Harbor of Separation Website Design

The primary objectives of this website is lead generation, create authority and enhance trust factor so that potential clients utilize Harbor of Separation services.

In an effort to provide prospects with a comprehensive explanation of the company’s services, Harbor of Separation will be creating a new website to provide, a user-friendly experience that will lead a person onto the right pathway where they will find tailored information depending on the stage they are in: Thinking of Divorce, Ready to Move Forward, and Recently Divorced.

Visitors will land on the homepage, which will give them the opportunity to select from the three types of personas shown. Messaging will be written specifically for each persona type, a lead-gen form will be present throughout the entire site, and a free downloadable form will be provided to them.

Once the lead gen form is submitted, information will be sent to Harbor of Separation consultant, who will follow up with the prospect.

Social Integration with website continue to prove Harbor of Separation authority and expertise.

Target Market(s)

Individuals who are considering or our in the process of divorce find themselves in a state of trying to make sense of it all. They lack the knowledge they need concerning the divorce process. Both men and women are typically scared of the unknown and financial loss. Due to the emotional stress they hire an attorney quickly that may not be suitable to their personality and/or situation.

Both men and women need an unbiased and informed partner that can guide them in the right direction. Time is their most precious commodity; making costly mistakes might ruin their financial situation, enhance their stress levels and prolong the divorce process. Both parties are looking for the right answers, the right professional divorce team, i.e. lawyer, mediator, financial planner, etc. to help them get their lives back in order.

Demographics
• Men and Women
• Ages 36 to 55
• Income: 80K+ per person or $150K+ combined
• Working Professionals: dentist, managers, creative directors, bankers, etc.

Industry/Entity Type

It Company

Requirements
Must have
• Visual Feeling
• The look and feel should represent a feeling of trust and reliability.
• Use colors from the logo.
• Please select images from Q-Frame Images
• Please refer to wireframes to see where images should be placed
• Calls To Action should stand out on each page.

Use the new logo Harbor of Separation Logo and tagline: Answers, Referrals, Support.

Please use the following URL: www.harborofseparation-example.com

```html
<!DOCTYPE html>
<html lang="en">
<head>
<meta charset="utf-8">
<title>Harbor of Separation — Home</title>
<link rel="stylesheet" href="https://fonts.googleapis.com/css2?family=Questrial&family=Arimo:wght@400&display=swap">
<style>
  :root {
    --brand-blue: #4a86c5;
    --brand-green: #5a9330;
    --brand-green-light: #7aa85a;
    --tile-title: #dcedc9;
    --hero-grey: #e8e8e8;
    --press-fill: #c5dbb5;
    --press-border: #a9c79a;
    --text-dark: #555555;
    --text-body: #444444;
    --rule: #d4d4d4;
    --white: #ffffff;
    --cta-text: #c9e3a5;
  }
  * { box-sizing: border-box; margin: 0; padding: 0; }
  html, body { width: 1200px; height: 1000px; overflow: hidden; background: var(--white); }
  body { position: relative; font-family: "Questrial", "Century Gothic", sans-serif; color: var(--text-dark); }
  .abs { position: absolute; }

  /* Brand */
  .brand { left: 290px; top: 8px; display: flex; flex-direction: column; align-items: flex-start; gap: 6px; }
  .brand-mark { width: 50px; height: 38px; margin-left: 34px; background: var(--brand-green); }
  .brand-name { font-size: 15px; color: var(--brand-green); letter-spacing: 0.2px; white-space: nowrap; }

  /* Hero */
  .hero { left: 290px; top: 78px; width: 634px; height: 178px; background: var(--hero-grey); }
  .call-us { left: 715px; top: 94px; font-size: 34px; line-height: 40px; color: var(--brand-blue); }

  /* Navigation */
  .main-nav { left: 99px; top: 265px; width: 1001px; height: 30px; background: var(--brand-blue); }
  .main-nav a { position: absolute; top: 9px; font-size: 9px; color: var(--white); text-decoration: none; }

  /* Persona tiles */
  .tile { color: var(--white); }
  .tile.dark { background: var(--brand-green); }
  .tile.light { background: var(--brand-green-light); }
  .tile-title { position: absolute; left: 13px; top: 16px; font-size: 13px; color: var(--tile-title); }
  .tile-link { position: absolute; right: 8px; bottom: 9px; font-size: 13px; color: var(--white); }

  /* Call to action panel */
  .cta-panel { left: 612px; top: 308px; width: 312px; height: 196px; background: var(--brand-blue); border-radius: 6px; text-align: center; }
  .cta-copy { margin-top: 38px; font-size: 16.5px; line-height: 20px; color: var(--cta-text); }
  .cta-button { position: absolute; left: 49px; top: 100px; width: 225px; height: 44px; background: var(--white); border-radius: 5px; font-size: 10px; line-height: 44px; color: var(--brand-blue); }

  /* Intro copy */
  .intro { left: 292px; top: 522px; width: 634px; font-family: "Arimo", Arial, sans-serif; font-size: 7px; line-height: 12px; color: var(--text-body); }
  .intro p { margin-bottom: 10px; }

  /* Press */
  .press-heading { left: 291px; top: 674px; font-size: 14px; color: var(--text-dark); }
  .press-slot { top: 701px; width: 145px; height: 98px; background: var(--press-fill); border: 1px solid var(--press-border); border-radius: 8px; }

  /* Footer */
  .footer-rule { top: 826px; width: 1px; height: 172px; background: var(--rule); }
  .footer-heading { top: 823px; font-size: 13px; line-height: 14px; color: var(--text-dark); }
  .quick-links { left: 291px; top: 859px; list-style: none; font-size: 10px; line-height: 12px; color: var(--text-dark); }
  .testimonial-card { left: 418px; top: 860px; width: 127px; height: 129px; background: var(--brand-blue); color: var(--white); }
  .testimonial-title { position: absolute; left: 0; top: 6px; width: 100%; text-align: center; font-size: 12px; }
  .testimonial-quote { position: absolute; left: 12px; top: 28px; width: 110px; font-family: "Arimo", Arial, sans-serif; font-size: 7px; line-height: 12px; }
  .testimonial-next { position: absolute; left: 68px; top: 103px; width: 47px; height: 20px; background: var(--white); color: var(--brand-blue); font-size: 10px; line-height: 20px; text-align: center; }
  .contact-block { left: 597px; top: 859px; font-size: 9px; color: var(--text-dark); }
  .contact-block .copyright { margin-bottom: 9px; }
  .contact-block address { font-style: normal; font-size: 8px; line-height: 9px; padding-left: 2px; margin-bottom: 22px; }
  .contact-block .phone { font-size: 8px; padding-left: 2px; }
  .field { left: 735px; width: 189px; height: 24px; border: 1px solid #dddddd; font-size: 7px; color: #999999; padding: 7px 11px; }
  .signup { left: 854px; top: 930px; width: 70px; height: 23px; background: var(--brand-blue); color: var(--white); font-size: 8px; line-height: 23px; text-align: center; }
  .follow { left: 735px; top: 970px; font-size: 10px; color: var(--text-dark); }
  .social-square { top: 967px; width: 16px; height: 16px; border-radius: 2px; }
</style>
</head>
<body>

  <header>
    <div class="abs brand">
      <span class="brand-mark"></span>
      <span class="brand-name">Harbor of Separation</span>
    </div>
    <div class="abs hero" role="img" aria-label="Hero photograph area for a calm, reassuring lifestyle image"></div>
    <p class="abs call-us">Call Us<br>555.010.2284</p>
  </header>

  <nav class="abs main-nav">
    <a href="#" style="left:192px">About Us</a>
    <a href="#" style="left:277px">Services</a>
    <a href="#" style="left:354px">Resources</a>
    <a href="#" style="left:435px">Take Control</a>
    <a href="#" style="left:520px">Contact Us</a>
  </nav>

  <main>
    <section class="personas">
      <a class="abs tile dark" style="left:290px;top:307px;width:157px;height:92px">
        <span class="tile-title">Thinking of Divorce ?</span><span class="tile-link">Learn More</span>
      </a>
      <a class="abs tile light" style="left:453px;top:308px;width:154px;height:91px">
        <span class="tile-title" style="left:6px">Need To do Something ?</span><span class="tile-link">Learn More</span>
      </a>
      <a class="abs tile light" style="left:290px;top:409px;width:157px;height:94px">
        <span class="tile-title">Recently Divorced ?</span><span class="tile-link" style="right:17px">Learn More</span>
      </a>
      <a class="abs tile dark" style="left:453px;top:409px;width:154px;height:94px">
        <span class="tile-title" style="left:7px">Financial Help ?</span><span class="tile-link" style="right:11px">Learn More</span>
      </a>
    </section>

    <section class="abs cta-panel">
      <p class="cta-copy">Take the mystery out of Divorce.<br>Find out what&nbsp; you need to&nbsp; know !</p>
      <a class="cta-button">Schedule Your FREE Counsultation.</a>
    </section>

    <section class="abs intro">
      <p>Lorem ipsum dolor sit amet,&nbsp; consectetuer adipiscing Lorem ipsum dolor sit amet, consectetuer adipiscing Lorem ipsum dolor sit amet, Lorem ipsum dolor sit amet,&nbsp; consectetuer adipiscing Lorem ipsum dolor sit amet, consectetuer adipiscing Lorem ipsum dolor sit amet, Lorem ipsum dolor sit amet,&nbsp; consectetuer adipiscing Lorem ipsum dolor sit amet, consectetuer adipiscing Lorem ipsum dolor sit amet,</p>
      <p>Lorem ipsum dolor sit amet,&nbsp; consectetuer adipiscing Lorem ipsum dolor sit amet, consectetuer adipiscing Lorem ipsum dolor sit amet, Lorem ipsum dolor sit amet,&nbsp; consectetuer adipiscing Lorem ipsum dolor sit amet, consectetuer adipiscing Lorem ipsum dolor sit amet, Lorem ipsum dolor sit amet,&nbsp; consectetuer adipiscing Lorem ipsum dolor sit amet, consectetuer adipiscing Lorem ipsum dolor sit amet,</p>
      <p>Lorem ipsum dolor sit amet,&nbsp; consectetuer adipiscing Lorem ipsum dolor sit amet, consectetuer adipiscing Lorem ipsum dolor sit amet, Lorem ipsum dolor sit amet,&nbsp; consectetuer adipiscing Lorem ipsum dolor sit amet, consectetuer adipiscing Lorem ipsum dolor sit amet, Lorem ipsum dolor sit amet,&nbsp; consectetuer adipiscing Lorem ipsum dolor sit amet, consectetuer adipiscing Lorem ipsum dolor sit amet,</p>
    </section>

    <section class="press">
      <h2 class="abs press-heading" style="font-weight:400">As Seen on:</h2>
      <div class="abs press-slot" style="left:289px"></div>
      <div class="abs press-slot" style="left:453px"></div>
      <div class="abs press-slot" style="left:616px"></div>
      <div class="abs press-slot" style="left:780px"></div>
    </section>
  </main>

  <footer>
    <span class="abs footer-rule" style="left:395px"></span>
    <span class="abs footer-rule" style="left:565px"></span>
    <span class="abs footer-rule" style="left:723px"></span>

    <h3 class="abs footer-heading" style="left:291px;font-weight:400">Quick Links</h3>
    <ul class="abs quick-links">
      <li>About Us</li><li>Services</li><li>Testimonials</li><li>Resources</li>
      <li>Take Control</li><li>Contact Us</li><li>Privacy Policy</li><li>Terms</li><li>Disclaimers</li>
    </ul>

    <h3 class="abs footer-heading" style="left:418px;width:120px;text-align:center;font-weight:400">What Peoples<br>are Saying</h3>
    <div class="abs testimonial-card">
      <span class="testimonial-title">Testimonials</span>
      <p class="testimonial-quote">Lorem ipsum dolor sit amet, consectetuer adipiscing Lorem ipsum dolor sit amet, consectetuer adipiscing Lorem ipsum dolor sit amet,</p>
      <span class="testimonial-next">Next &gt;</span>
    </div>

    <h3 class="abs footer-heading" style="left:600px;font-weight:400">Get in Touch</h3>
    <div class="abs contact-block">
      <p class="copyright">Copyright 2013</p>
      <address>Harbor of Separation<br>4120 Coral Bend Road Ste 210<br>Bayview, Florida 33000</address>
      <p class="phone">555. 010. 2284</p>
    </div>

    <h3 class="abs footer-heading" style="left:737px;width:200px;text-align:center;font-weight:400">Harbor of Separation Newsletter<br>Educate Yourself</h3>
    <div class="abs field" style="top:860px">First Name</div>
    <div class="abs field" style="top:896px">Email</div>
    <div class="abs signup">Sign Up</div>
    <span class="abs follow">FOLLOW US</span>
    <span class="abs social-square" style="left:802px;background:#4a5f9a"></span>
    <span class="abs social-square" style="left:822px;background:#5bc0ea"></span>
  </footer>

</body>
</html>
```